Florabelle Packaging Design Project Hair Removal products

Florabelle is launching a New Hair Removal Sub Brand, under the Florabelle Brand .

This new hair removal range will include approx six products that are all designed to remove hair. These include hot wax, wax strips, depilitaory creams, hair removal lotion etc.

We are looking for a fresh new look and a sub brand name for the range. Currently we have a name Florabelle Sorbet Swish as a name option but we are not sold on this name so we would like to see other options . We would like the brand to use the same primary colours as our current florabelle brand. ie the pink and the blue but it should look different from the current range. I will email through all the pantones and logos on the brand. You can check out florabelle-example.co.za to see the current range

For the design we would like to see a design for a sticker that goes on a bottle as well as see how it translates on a box.

Target Market(s)

any female using hair removal products

Industry/Entity Type

Hair

Requirements
Must have
• simple design.

must use our colours

it must somehow portray that using our hair removal system is really quick, easy and effective

You can use images of legs on the packaging but it is not required.

all design must have the main brand logo "Florabelle" on the packaging but with regard to the sub name for the brand we are not sold on our name so we require that for one of your artwork options that you use our name "Sorbet Swish" for one of the designs , however we would also like you to come up with your own name for the hair removal range.

Florabelle logo is not dominant and can remain in the background.

```html
<!DOCTYPE html>
<html lang="en">
<head>
<meta charset="utf-8">
<title>Sorbet Swish – Hair removal tube</title>
<link rel="stylesheet" href="https://fonts.googleapis.com/css2?family=Pinyon+Script&family=Open+Sans:wght@400;700&display=swap">
<style>
  :root {
    --page: #ffffff;
    --outline: #3d4a52;
    --tube-light: #f2fafd;
    --tube-mid: #cfe8f2;
    --tube-deep: #a9d3e3;
    --script-teal: #1d97b3;
    --accent-pink: #e0407e;
    --accent-pink-soft: rgba(224, 64, 126, 0.55);
    --cap-light: #bfe6f0;
    --cap-mid: #3ab0c9;
    --cap-deep: #137f9b;
    --ink: #4a4f55;
    --white: #ffffff;
  }
  * { margin: 0; padding: 0; box-sizing: border-box; }
  html, body {
    width: 1200px;
    height: 2828px;
    overflow: hidden;
    background: var(--page);
  }
  .canvas {
    position: relative;
    width: 1200px;
    height: 2828px;
    overflow: hidden;
  }
  .tube-shape {
    position: absolute;
    inset: 0;
  }
  .floral-area {
    position: absolute;
    left: 560px;
    top: 440px;
    width: 520px;
    height: 1500px;
    border-radius: 260px 200px 240px 180px;
    background: radial-gradient(ellipse at 55% 45%, var(--accent-pink-soft) 0%, rgba(224,64,126,0.25) 55%, rgba(224,64,126,0) 78%);
  }
  .sub-brand {
    position: absolute;
    left: 380px;
    top: 1290px;
    transform: translate(-50%, -50%) rotate(-90deg);
    white-space: nowrap;
    font-family: "Pinyon Script", cursive;
    font-size: 330px;
    line-height: 1;
    color: var(--script-teal);
  }
  .brand-mark {
    position: absolute;
    left: 760px;
    top: 350px;
    display: flex;
    align-items: center;
    gap: 18px;
  }
  .brand-mark__dot {
    width: 64px;
    height: 64px;
    border-radius: 50%;
    background: var(--accent-pink);
  }
  .brand-mark__name {
    font-family: "Open Sans", sans-serif;
    font-weight: 400;
    font-size: 64px;
    color: var(--ink);
  }
  .product-tag {
    position: absolute;
    left: 820px;
    top: 2030px;
    width: 270px;
    height: 310px;
    background: var(--accent-pink);
    padding: 30px 24px;
    display: flex;
    align-items: center;
    justify-content: flex-end;
    text-align: right;
    font-family: "Open Sans", sans-serif;
    font-weight: 700;
    font-size: 62px;
    line-height: 1.2;
    color: var(--white);
  }
</style>
</head>
<body>
<main class="canvas">
  <svg class="tube-shape" width="1200" height="2828" viewBox="0 0 1200 2828" aria-hidden="true">
    <defs>
      <radialGradient id="tube-cloud-a" cx="0.3" cy="0.3" r="0.6">
        <stop offset="0" stop-color="var(--tube-light)"/>
        <stop offset="1" stop-color="var(--tube-mid)"/>
      </radialGradient>
      <radialGradient id="tube-cloud-b" cx="0.6" cy="0.75" r="0.35">
        <stop offset="0" stop-color="var(--tube-deep)" stop-opacity="0.8"/>
        <stop offset="1" stop-color="var(--tube-deep)" stop-opacity="0"/>
      </radialGradient>
      <radialGradient id="tube-cloud-c" cx="0.25" cy="0.55" r="0.3">
        <stop offset="0" stop-color="#ffffff" stop-opacity="0.9"/>
        <stop offset="1" stop-color="#ffffff" stop-opacity="0"/>
      </radialGradient>
      <linearGradient id="cap-shine" x1="0" y1="0" x2="1" y2="0">
        <stop offset="0" stop-color="var(--cap-deep)"/>
        <stop offset="0.3" stop-color="var(--cap-light)"/>
        <stop offset="0.55" stop-color="var(--cap-mid)"/>
        <stop offset="1" stop-color="var(--cap-deep)"/>
      </linearGradient>
    </defs>
    <g class="tube-body">
      <path d="M22 36 L1178 36 L1062 2545 L138 2545 Z" fill="url(#tube-cloud-a)"/>
      <path d="M22 36 L1178 36 L1062 2545 L138 2545 Z" fill="url(#tube-cloud-b)"/>
      <path d="M22 36 L1178 36 L1062 2545 L138 2545 Z" fill="url(#tube-cloud-c)"/>
      <path d="M22 36 L1178 36 L1062 2545 L138 2545 Z" fill="none" stroke="var(--outline)" stroke-width="4"/>
      <line class="tube-crimp" x1="26" y1="96" x2="1174" y2="96" stroke="var(--outline)" stroke-width="3"/>
    </g>
    <g class="tube-cap">
      <rect x="190" y="2545" width="820" height="255" rx="10" fill="url(#cap-shine)"/>
      <rect x="190" y="2740" width="820" height="60" rx="10" fill="var(--cap-deep)" opacity="0.55"/>
      <rect x="190" y="2545" width="820" height="255" rx="10" fill="none" stroke="var(--outline)" stroke-width="4"/>
    </g>
  </svg>

  <div class="floral-area" role="img" aria-label="Pink floral swirl ornament with leaves and blossoms"></div>

  <div class="brand-mark">
    <span class="brand-mark__dot"></span>
    <span class="brand-mark__name">Florabelle</span>
  </div>

  <h1 class="sub-brand">Sorbet Swish</h1>

  <p class="product-tag">Hair<br>removal<br>product</p>
</main>
</body>
</html>
```